Brindlewick Music Studio needs a promotional postcard design

We are looking for a postcard design for a small business that provides clients with private music lesson instruction. We are looking for a design that will convey the message of "music is fun for kids" that will appeal to parents and encourage them to sign up. We have a company logo that should be used and our color scheme is teal and turquoise. All of our contact info should be displayed as well.

Target Market(s)

Parents with young kids

Contact Information for Business Card

web: www.brindlewickmusicstudio.example
email: lessons@brindlewickmusicstudio.example
phone: 202-555-0147

Font styles to use
Serif
Sans Serif

Colors
33b8a4
86cfc6
0456a4
87cfc6

Requirements
Must have
• Music lessons in your home
• Creating little stars one at a time
• Sign Up Now
• Please use these images:
Nice to have
• Something like this sample postcard:

```html
<!DOCTYPE html>
<html lang="en">
<head>
<meta charset="utf-8">
<title>Brindlewick Music Studio – Postcard</title>
<link href="https://fonts.googleapis.com/css2?family=Prata&family=Raleway:wght@500;600;700&family=Courgette&family=Tinos&display=swap" rel="stylesheet">
<style>
  :root {
    --teal: #3fb3b4;
    --teal-deep: #2fa3a6;
    --teal-light: #86cfc6;
    --ink: #111111;
    --paper: #ffffff;
    --backdrop: #ece9e4;
    --mist: #dfe3e4;
  }
  html, body {
    margin: 0;
    padding: 0;
    width: 900px;
    height: 1200px;
    overflow: hidden;
    background: var(--backdrop);
  }
  .canvas { position: relative; width: 900px; height: 1200px; }

  .card {
    position: absolute;
    left: 92px;
    width: 716px;
    height: 419px;
    background: var(--paper);
    overflow: hidden;
    box-shadow: 0 2px 8px rgba(0,0,0,0.12);
  }
  .card--front { top: 157px; }
  .card--back { top: 637px; }

  /* Brand lockup */
  .brand { position: absolute; display: flex; align-items: center; z-index: 2; }
  .brand__dot {
    border-radius: 50%;
    background: var(--teal);
    flex: none;
  }
  .brand__text { color: var(--teal); }
  .brand__name {
    font-family: "Prata", serif;
    line-height: 1;
    white-space: nowrap;
  }
  .brand__sub {
    font-family: "Raleway", sans-serif;
    font-weight: 500;
    letter-spacing: 0.42em;
    text-transform: uppercase;
    white-space: nowrap;
  }
  .card--front .brand { left: 46px; top: 34px; }
  .card--front .brand__dot { width: 92px; height: 92px; margin-right: 18px; }
  .card--front .brand__name { font-size: 33px; }
  .card--front .brand__sub { font-size: 11.5px; margin-top: 10px; }

  .card--back .brand { left: 52px; top: 183px; }
  .card--back .brand__dot { width: 72px; height: 72px; margin-right: 18px; }
  .card--back .brand__name { font-size: 30px; }
  .card--back .brand__sub { font-size: 10px; margin-top: 6px; }

  /* Front message */
  .pitch {
    position: absolute;
    left: 36px;
    top: 138px;
    width: 330px;
    text-align: center;
    font-family: "Raleway", sans-serif;
    color: var(--teal);
  }
  .pitch__lead { font-size: 16px; font-weight: 500; letter-spacing: 0.04em; margin: 0; }
  .pitch__main { font-size: 21px; font-weight: 700; margin: 2px 0 0; }
  .pitch__lead + .pitch__main + .pitch__lead { margin-top: 16px; }
  .signup {
    display: flex;
    align-items: center;
    gap: 10px;
    margin-top: 20px;
    font-family: "Courgette", cursive;
    font-size: 23px;
    color: var(--teal);
  }
  .signup::before, .signup::after {
    content: "";
    flex: 1;
    height: 1px;
    background: var(--teal);
  }
  .contact {
    margin-top: 20px;
    font-size: 17px;
    font-weight: 500;
    line-height: 24px;
  }
  .contact p { margin: 0; white-space: nowrap; }
  .contact__phone { letter-spacing: 0.06em; font-size: 18px; }

  .photo {
    position: absolute;
    left: 386px;
    top: 0;
    width: 330px;
    height: 419px;
  }

  /* Back */
  .splash {
    position: absolute;
    left: 0;
    top: 0;
    width: 360px;
    height: 419px;
    background: radial-gradient(ellipse at 40% 45%, var(--mist) 0%, #eef0f0 55%, rgba(255,255,255,0) 80%);
  }
  .postcard-title {
    position: absolute;
    left: 278px;
    top: 34px;
    font-family: "Tinos", serif;
    font-size: 22px;
    font-weight: 400;
    letter-spacing: 0.18em;
    color: var(--ink);
    margin: 0;
  }
  .stamp-box {
    position: absolute;
    left: 582px;
    top: 33px;
    width: 88px;
    height: 88px;
    border: 1.5px solid var(--ink);
  }
  .divider {
    position: absolute;
    left: 356px;
    top: 108px;
    width: 1.5px;
    height: 254px;
    background: var(--ink);
  }
  .divider::before {
    content: "";
    position: absolute;
    left: -3px;
    top: -3px;
    width: 7px;
    height: 7px;
    border-radius: 50%;
    background: var(--ink);
  }
  .deliver-label {
    position: absolute;
    left: 372px;
    top: 133px;
    margin: 0;
    font-family: "Tinos", serif;
    font-size: 15px;
    letter-spacing: 0.08em;
    color: var(--ink);
  }
  .address-line {
    position: absolute;
    left: 372px;
    width: 302px;
    height: 1.5px;
    background: var(--ink);
  }
</style>
</head>
<body>
<div class="canvas">

  <section class="card card--front">
    <div class="brand">
      <span class="brand__dot"></span>
      <div class="brand__text">
        <div class="brand__name">Brindlewick</div>
        <div class="brand__sub">Music Studio</div>
      </div>
    </div>

    <div class="pitch">
      <p class="pitch__lead">MUSIC LESSONS FOR</p>
      <p class="pitch__main">BEGINNERS IN YOUR HOME</p>
      <p class="pitch__lead">CREATING</p>
      <p class="pitch__main">LITTLE ROCK STARS</p>
      <div class="signup">Sign Up Now</div>
      <div class="contact">
        <p class="contact__phone">202 · 555 · 0147</p>
        <p>lessons@brindlewickmusicstudio.example</p>
        <p>www.brindlewickmusicstudio.example</p>
      </div>
    </div>

    <svg class="photo" viewBox="0 0 330 419" role="img" aria-label="Photo of a smiling young girl playing the violin in front of teal swooshes and piano keys">
      <defs>
        <linearGradient id="photoTone" x1="0" y1="0" x2="1" y2="1">
          <stop offset="0" stop-color="#f4efec"/>
          <stop offset="0.5" stop-color="#d9c6bd"/>
          <stop offset="1" stop-color="#b9b3b5"/>
        </linearGradient>
      </defs>
      <rect x="0" y="0" width="330" height="419" fill="#ffffff"/>
      <rect x="20" y="0" width="200" height="419" fill="url(#photoTone)"/>
      <rect x="278" y="0" width="52" height="419" fill="#e9e9e9"/>
      <path d="M190 0 C 300 60, 270 200, 200 300 C 170 350, 175 400, 190 419 L 250 419 C 230 380, 240 320, 280 240 C 320 150, 300 40, 240 0 Z" fill="var(--teal)"/>
      <path d="M230 0 C 300 50, 300 150, 260 240 C 230 320, 240 390, 255 419 L 278 419 C 262 380, 262 320, 290 240 C 320 150, 310 40, 262 0 Z" fill="var(--teal-light)"/>
    </svg>
  </section>

  <section class="card card--back">
    <div class="splash" role="img" aria-label="Soft grey watercolour splash with faint music notes"></div>
    <div class="brand">
      <span class="brand__dot"></span>
      <div class="brand__text">
        <div class="brand__name">Brindlewick</div>
        <div class="brand__sub">Music Studio</div>
      </div>
    </div>

    <h2 class="postcard-title">POSTCARD</h2>
    <div class="stamp-box"></div>
    <div class="divider"></div>
    <p class="deliver-label">DELIVER TO :</p>
    <div class="address-line" style="top:221px"></div>
    <div class="address-line" style="top:268px"></div>
    <div class="address-line" style="top:314px"></div>
    <div class="address-line" style="top:361px"></div>
  </section>

</div>
</body>
</html>
```